Business Card

We are looking to re-create our business card. Attached is the company logo. we would like it to be back and front. for example one side with the persons information and the other side with the company logo. Be as creative as you would like but also keep in mind, we are a Health Insurance company and we need to look professional as well.
Industry/Entity Type
Business

```html
<!DOCTYPE html>
<html lang="en">
<head>
<meta charset="utf-8">
<title>Meridian Health Cover — Business Card</title>
<link rel="stylesheet" href="https://fonts.googleapis.com/css2?family=Source+Sans+3:wght@400;600&display=swap">
<style>
  :root {
    --stage: #2b2b2b;
    --brand-blue: #0093d1;
    --accent-blue: #1a8fc8;
    --card-light: #efefef;
    --text-grey: #5a5a5a;
    --rule-grey: #9a9a9a;
    --white: #ffffff;
  }
  * { margin: 0; padding: 0; box-sizing: border-box; }
  html, body {
    width: 1200px; height: 900px; overflow: hidden;
    background: var(--stage);
    font-family: "Source Sans 3", "Helvetica Neue", Arial, sans-serif;
  }
  .canvas { position: relative; width: 1200px; height: 900px; }

  .card { position: absolute; top: 323px; width: 447px; height: 255px; }
  .card--front { left: 144px; background: var(--brand-blue); }
  .card--back { left: 611px; background: var(--card-light); }

  .brand { position: absolute; display: flex; align-items: center; gap: 10px; }
  .brand__mark { width: 14px; height: 14px; }
  .brand__name { font-weight: 600; white-space: nowrap; }

  .card--front .brand { left: 41px; top: 184px; }
  .card--front .brand__mark { background: var(--white); }
  .card--front .brand__name { color: var(--white); font-size: 25px; }
  .card--front .brand__rule {
    position: absolute; left: 140px; top: 166px; width: 1px; height: 61px;
    background: rgba(255,255,255,0.7);
  }
  .card--front .website {
    position: absolute; left: 41px; top: 215px;
    color: var(--white); font-size: 12px; letter-spacing: 0.2px;
  }

  .card--back .brand { left: 40px; top: 66px; }
  .card--back .brand__mark { background: var(--accent-blue); }
  .card--back .brand__name { color: var(--accent-blue); font-size: 20px; }

  .person { position: absolute; left: 40px; top: 146px; white-space: nowrap; }
  .person__name { color: var(--accent-blue); font-size: 19px; }
  .person__role { color: var(--text-grey); font-size: 11px; margin-left: 3px; }

  .contact { position: absolute; top: 187px; font-size: 10px; line-height: 14.5px; color: var(--text-grey); }
  .contact--address { left: 40px; }
  .contact--lines { left: 207px; }
  .contact__label { color: var(--accent-blue); }
  .contact__rule {
    position: absolute; left: 189px; top: 187px; width: 1px; height: 42px;
    background: var(--rule-grey);
  }
</style>
</head>
<body>
<main class="canvas">
  <section class="card card--front" aria-label="Card front">
    <div class="brand">
      <span class="brand__mark"></span>
      <span class="brand__name">Meridian Health Cover</span>
    </div>
    <p class="website">www.meridianhealthcover.com</p>
  </section>

  <section class="card card--back" aria-label="Card back">
    <div class="brand">
      <span class="brand__mark"></span>
      <span class="brand__name">Meridian Health Cover</span>
    </div>
    <p class="person"><span class="person__name">Laura Benton,</span><span class="person__role">Managed Services</span></p>
    <address class="contact contact--address" style="font-style:normal">
      Meridian Health Cover Pty Ltd<br>
      Level 4, 88 Sample Road<br>
      Sydney, NSW 0000 Australia
    </address>
    <span class="contact__rule"></span>
    <p class="contact contact--lines">
      <span class="contact__label">tel:</span> 1300 555 0192<br>
      <span class="contact__label">fax:</span> 61 0 555 0193<br>
      <span class="contact__label">email:</span> service@meridianhealthcover.com
    </p>
  </section>
</main>
</body>
</html>
```